ORVALIS MED -DIAGNOSTIC CENTRE FOR IMAGES

Our Activity provides diagnostic services for images (RMI, Tac, RX, Ultrasound etc.)
We would like to create a broschure that illustrates our services.
We would like to give maximum attention to the Diagnostic service dedicated to "HEART", therefore maximum evidence to the world of Cardiology.
In the background we would like to highlight the other diagnostic services dedicated to the Rest of the Body (Brain, Knees Legs etc.)
Target Market(s)
PERSONS WHO NEED TO PERFORM DIAGNOSTIC TESTS (MRI, CT, ULTRASOUND, RX ETC.)
Industry/Entity Type
HEALTH
Requirements
Must have
- The company logo, must have diagnostic images (MRI, CT, X-ray, ultrasound), must be simple and intuitive, which is harmonious with the colors of our company logo
Should not have
- Colours that are not in harmony with our company logo

```html
<!DOCTYPE html>
<html lang="en">
<head>
<meta charset="utf-8">
<title>Orvalis Med – Diagnostic Brochure</title>
<link rel="stylesheet" href="https://fonts.googleapis.com/css2?family=Roboto:wght@400;500;700;900&display=swap">
<style>
:root{
  --teal:#2aa99b;
  --teal-dark:#1f9a8c;
  --navy:#173a5e;
  --blue:#2667ad;
  --ink:#222a30;
  --page:#efefef;
  --page-right:#eaebeb;
  --mist:#d9e9ef;
  --night:#1c1e1f;
  --ground:#f6f6f6;
}
*{margin:0;padding:0;box-sizing:border-box}
html,body{width:941px;height:1200px;overflow:hidden;background:var(--ground)}
body{position:relative;font-family:"Roboto",Arial,sans-serif;color:var(--ink)}
.abs{position:absolute}
.spread{position:absolute;left:113px;width:754px;box-shadow:0 6px 14px rgba(0,0,0,.12)}
.spread--cover{top:70px;height:508px}
.spread--inside{top:650px;height:500px}
.page{position:absolute;top:0;height:100%;overflow:hidden}
.page--left{left:0;width:377px;background:var(--page)}
.page--right{left:377px;width:377px;background:var(--page-right)}
.mist{position:absolute;background:var(--mist);border-radius:6px}
.bar{position:absolute;border-radius:3px}
.bar--teal{background:var(--teal)}
.bar--navy{background:var(--navy)}
.frame{position:absolute;border:1.5px solid var(--navy);border-radius:8px}
.ring{position:absolute;border:2px solid var(--teal);border-radius:50%}
.dots{position:absolute;background-image:radial-gradient(circle,var(--navy) 1.1px,transparent 1.4px);background-size:8px 8px}
.photo{position:absolute;border-radius:10px}
.wordmark{position:absolute;color:var(--teal);font-weight:500;letter-spacing:.5px;white-space:nowrap;display:flex;align-items:center;gap:6px}
.wordmark i{display:block;border-radius:50%;background:var(--teal)}
.service{position:absolute;width:80px;text-align:center;font-size:8.6px;font-weight:700;line-height:1.15;color:var(--ink)}
.service__tile{width:41px;height:41px;margin:0 auto 4px;background:var(--teal);border-radius:5px;display:flex;align-items:center;justify-content:center;box-shadow:0 2px 4px rgba(0,0,0,.12)}
.contact__title{font-size:12px;font-weight:700;color:var(--navy)}
.contact__cta{font-size:12px;font-weight:700;color:var(--teal)}
.contact__line{font-size:8.5px;color:var(--ink);line-height:1.4}
.headline{font-weight:700;line-height:1}
.pill{position:absolute;height:15px;padding:0 7px;border-radius:3px;font-size:8.5px;line-height:15px;color:#fff;white-space:nowrap}
.pill--blue{background:var(--blue);transform:translateX(-50%)}
.pill--teal{background:var(--teal)}
.tri{position:absolute;width:0;height:0;border-left:6px solid transparent;border-right:6px solid transparent;border-bottom:8px solid var(--teal)}
.section-title{position:absolute;font-size:17px;font-weight:700;line-height:1.25}
.section-title .navy{color:var(--navy)}
.section-title .teal{color:var(--teal)}
.lead{position:absolute;font-size:8.7px;line-height:1.38;color:var(--ink);hyphens:auto}
.feature{position:absolute;left:150px;width:190px}
.feature__tag{display:inline-block;background:var(--teal);color:#fff;font-size:10px;font-weight:700;padding:1px 5px;border-radius:2px;margin-bottom:1px}
.feature__text{font-size:8.2px;line-height:1.22;text-align:justify;hyphens:auto}
.benefits{position:absolute;left:150px;top:423px;font-size:10px;font-weight:700;color:var(--navy)}
.perks{position:absolute;left:10px;top:307px;width:330px;height:164px;background:var(--night);border-radius:8px}
.perk{position:absolute;width:140px;font-size:8.5px;line-height:1.2;color:#fff;padding-left:16px}
.perk svg{position:absolute;left:0;top:1px}
</style>
</head>
<body>

<!-- Cover spread -->
<section class="spread spread--cover">
  <div class="page page--left">
    <div class="mist" style="left:-10px;top:-10px;width:60px;height:115px"></div>
    <div class="frame" style="left:46px;top:-10px;width:66px;height:33px"></div>
    <div class="bar bar--teal" style="left:21px;top:47px;width:124px;height:6px"></div>
    <div class="ring" style="left:272px;top:28px;width:18px;height:18px"></div>
    <div class="photo" role="img" aria-label="MRI scanner in a bright clinical room with a light blue patient table" style="left:33px;top:66px;width:292px;height:197px;background:linear-gradient(165deg,#d5dbe2 0%,#eef1f4 40%,#dfe6ec 62%,#9ccbe6 100%)"></div>
    <div class="wordmark" style="left:72px;top:148px;font-size:26px"><i style="width:10px;height:10px"></i>ORVALIS MED</div>

    <div class="mist" style="left:15px;top:295px;width:16px;height:58px"></div>
    <div class="mist" style="left:-5px;top:316px;width:56px;height:16px"></div>

    <div class="service" style="left:44px;top:240px">
      <div class="service__tile"><svg width="22" height="22" viewBox="0 0 24 24" fill="none" stroke="#fff" stroke-width="1.6" stroke-linejoin="round" stroke-linecap="round"><path d="M12 20s-8-5-8-11a4 4 0 0 1 8-1 4 4 0 0 1 8 1c0 6-8 11-8 11z"/><path d="M5 12h4l1.5-3 2 5 1.5-2h5"/></svg></div>
      Cardiology<br>Services</div>
    <div class="service" style="left:140px;top:240px">
      <div class="service__tile"><svg width="22" height="22" viewBox="0 0 24 24" fill="none" stroke="#fff" stroke-width="1.6" stroke-linecap="round"><path d="M12 5a4 4 0 0 0-7 3 4 4 0 0 0 1 7 3 3 0 0 0 6 1V5z"/><path d="M12 5a4 4 0 0 1 7 3 4 4 0 0 1-1 7 3 3 0 0 1-6 1"/></svg></div>
      Neurology<br>Scans</div>
    <div class="service" style="left:234px;top:240px">
      <div class="service__tile"><svg width="22" height="22" viewBox="0 0 24 24" fill="none" stroke="#fff" stroke-width="1.6" stroke-linecap="round"><rect x="5" y="3" width="14" height="18" rx="2"/><circle cx="12" cy="8" r="1.6"/><path d="M10 11h4v4h-1v3h-2v-3h-1z"/></svg></div>
      Full-body<br>Scans</div>
    <div class="service" style="left:93px;top:312px">
      <div class="service__tile"><svg width="22" height="22" viewBox="0 0 24 24" fill="none" stroke="#fff" stroke-width="1.6" stroke-linecap="round"><rect x="4" y="3" width="16" height="18" rx="2"/><path d="M10 6v4a2 2 0 0 0 4 0V6M10 18v-3a2 2 0 0 1 4 0v3"/></svg></div>
      Orthopedic<br>Scans</div>
    <div class="service" style="left:188px;top:312px">
      <div class="service__tile"><svg width="22" height="22" viewBox="0 0 24 24" fill="none" stroke="#fff" stroke-width="1.6" stroke-linecap="round" stroke-linejoin="round"><circle cx="12" cy="6" r="3"/><path d="M5 19a7 7 0 0 1 14 0"/><path d="M8 15h2l1 2 2-4 1 2h2"/></svg></div>
      Customized<br>Care</div>

    <div class="dots" style="left:309px;top:337px;width:34px;height:34px"></div>
    <div class="ring" style="left:346px;top:395px;width:20px;height:20px"></div>

    <div class="abs" style="left:17px;top:402px">
      <div class="contact__title">FOR APPOINTMENTS AND INQUIRIES</div>
      <div class="contact__cta" style="margin-top:3px">CONTACT US TODAY!</div>
      <div class="contact__line" style="margin:7px 0 0 4px">Addressline 1<br>Addressline 2</div>
      <div class="contact__line" style="margin:11px 0 0 4px">Phone no: +12 5550 147</div>
    </div>
    <div class="mist" style="left:294px;top:451px;width:100px;height:70px;border-radius:10px"></div>
    <div class="frame" style="left:143px;top:486px;width:66px;height:40px"></div>
    <div class="wordmark" style="left:252px;top:472px;font-size:12px;gap:3px"><i style="width:5px;height:5px"></i>ORVALIS MED</div>
  </div>

  <div class="page page--right">
    <div class="mist" style="left:42px;top:0;width:21px;height:70px"></div>
    <div class="mist" style="left:12px;top:21px;width:77px;height:21px"></div>
    <div class="bar bar--navy" style="left:234px;top:20px;width:143px;height:7px"></div>
    <div class="mist" style="left:318px;top:58px;width:60px;height:120px;border-radius:14px"></div>
    <div class="frame" style="left:333px;top:144px;width:50px;height:66px"></div>

    <div class="wordmark" style="left:126px;top:52px;font-size:19px;gap:4px"><i style="width:7px;height:7px"></i>ORVALIS MED</div>
    <div class="headline abs" style="left:0;width:357px;top:106px;text-align:center;font-size:23px;font-weight:500;color:#1d82a8">YOUR HEART</div>
    <div class="headline abs" style="left:0;width:357px;top:131px;text-align:center;font-size:32px;font-weight:900;color:var(--teal)">MATTERS</div>
    <div class="abs" style="left:0;width:357px;top:165px;text-align:center;font-size:10.5px;color:var(--ink)">Diagnostic Services for a Healthier You</div>

    <div class="tri" style="left:25px;top:156px"></div>
    <div class="tri" style="left:25px;top:168px"></div>
    <div class="tri" style="left:25px;top:180px"></div>
    <div class="tri" style="left:25px;top:192px"></div>

    <div class="abs" role="img" aria-label="Smiling doctor in a white coat with a stethoscope holding a small red heart, set in a teal circle" style="left:88px;top:242px;width:181px;height:181px;border-radius:50%;background:radial-gradient(circle at 50% 40%,#f1f3f4 0%,#dfe7e8 30%,#6cc3b9 62%,var(--teal-dark) 100%)"></div>
    <div class="abs" style="left:304px;top:259px;width:41px;height:41px;border-radius:5px;background:var(--teal)"></div>

    <div class="pill pill--blue" style="left:95px;top:437px">Highly Experienced Staff</div>
    <div class="pill pill--blue" style="left:253px;top:436px">Knowledgeable Support Staff</div>
    <div class="pill pill--blue" style="left:95px;top:463px">Friendly Environment</div>
    <div class="pill pill--blue" style="left:253px;top:462px">Cutting-edge Systems</div>
    <div class="bar bar--teal" style="left:9px;top:496px;width:125px;height:3px"></div>
  </div>
</section>

<!-- Inside spread -->
<section class="spread spread--inside">
  <div class="page page--left">
    <div class="mist" style="left:-5px;top:-5px;width:45px;height:14px"></div>
    <div class="frame" style="left:17px;top:-10px;width:67px;height:18px"></div>
    <svg class="abs" style="left:313px;top:24px" width="14" height="14" viewBox="0 0 14 14" stroke="var(--navy)" stroke-width="1.2"><path d="M7 0v5M7 9v5M0 7h5M9 7h5"/></svg>
    <h2 class="section-title" style="left:21px;top:28px"><span class="navy">OUR MAIN FOCUS</span><br><span class="teal">CARDIOLOGY EXCELLENCE</span></h2>
    <p class="lead" style="left:21px;top:80px;width:326px">At Orvalis Med, we are dedicated to delivering exceptional cardiac care to safeguard your heart health. Our cutting-edge technology and skilled medical professionals are committed to providing you with accurate diagnoses and effective treatments, ensuring your heart remains in the best possible condition.</p>

    <div class="photo" role="img" aria-label="Cart-mounted ultrasound machine with monitor showing a scan" style="left:21px;top:160px;width:117px;height:146px;background:linear-gradient(180deg,#6f7780 0%,#b9c0c6 35%,#e4e7e9 65%,#8a9096 100%);border-radius:6px"></div>
    <div class="photo" role="img" aria-label="Digital X-ray system with wall stand and patient table" style="left:21px;top:318px;width:105px;height:126px;background:linear-gradient(180deg,#e6e8ea 0%,#d3d8dc 55%,#eceeef 100%);border-radius:6px"></div>

    <div class="feature" style="top:152px"><span class="feature__tag">Cardiac Imaging</span><p class="feature__text">We offer advanced cardiac imaging services, including state-of-the-art MRI and CT scans, to provide a comprehensive view of your heart's structure and function</p></div>
    <div class="feature" style="top:220px"><span class="feature__tag">Electrocardiography (ECG/EKG)</span><p class="feature__text">Our ECG/EKG tests accurately monitor your heart's electrical activity, helping to diagnose arrhythmias, heart attacks, and other cardiac conditions.</p></div>
    <div class="feature" style="top:290px"><span class="feature__tag">Echocardiography</span><p class="feature__text">Our high-resolution echocardiography allows us to assess your heart's chambers, valves, and blood flow, aiding in the detection of heart diseases.</p></div>
    <div class="feature" style="top:359px"><span class="feature__tag">Holter Monitoring</span><p class="feature__text">For continuous heart monitoring, our Holter monitors record your heart's activity over 24 hours or more, helping us identify irregularities that may go unnoticed in shorter tests.</p></div>

    <div class="benefits">Other Benefits</div>
    <div class="mist" style="left:268px;top:452px;width:12px;height:32px"></div>
    <div class="mist" style="left:252px;top:462px;width:44px;height:12px"></div>
    <div class="pill pill--teal" style="left:150px;top:440px">Stress Testing</div>
    <div class="pill pill--teal" style="left:228px;top:440px">Coronary Angiography</div>
    <div class="pill pill--teal" style="left:150px;top:461px">Cardiac Consultations</div>
    <div class="bar bar--navy" style="left:0;top:483px;width:120px;height:6px"></div>
  </div>

  <div class="page page--right">
    <div class="mist" style="left:48px;top:0;width:20px;height:40px"></div>
    <div class="mist" style="left:20px;top:14px;width:78px;height:20px"></div>
    <div class="bar bar--navy" style="left:234px;top:11px;width:143px;height:7px"></div>
    <div class="dots" style="left:325px;top:28px;width:26px;height:26px"></div>
    <div class="abs" style="left:320px;top:44px;width:17px;height:17px;border-radius:3px;background:var(--teal)"></div>

    <h2 class="section-title" style="left:13px;top:27px"><span class="navy">COMPREHENSIVE DIAGNOSTICS</span><br><span class="teal">BEYOND CARDIOLOGY</span></h2>
    <p class="lead" style="left:13px;top:79px;width:330px">In addition to our specialized cardiology services, we offer a wide range of comprehensive diagnostic services to address your healthcare needs holistically. At [Your Company Name], we believe in the importance of thorough diagnostics to ensure your overall well-being. Our diagnostic services include:</p>

    <div class="photo" role="img" aria-label="White CT scanner with gantry ring and motorised patient table" style="left:15px;top:158px;width:176px;height:115px;background:linear-gradient(135deg,#f3f4f5 0%,#dde2e5 50%,#eef0f1 100%);border-radius:8px"></div>

    <div class="pill pill--teal" style="left:199px;top:159px">Neuroimaging</div>
    <div class="pill pill--teal" style="left:281px;top:159px">Ultrasound</div>
    <div class="pill pill--teal" style="left:199px;top:183px">Musculoskeletal Imaging</div>
    <div class="pill pill--teal" style="left:199px;top:206px">Abdominal Imaging</div>
    <div class="pill pill--teal" style="left:199px;top:229px">Multi-Specialty Consultations</div>
    <div class="pill pill--teal" style="left:199px;top:252px">X-rays (RX)</div>

    <div class="perks">
      <div class="perk" style="left:20px;top:22px"><svg width="9" height="8" viewBox="0 0 10 8" fill="none" stroke="var(--teal)" stroke-width="2"><path d="M1 4l3 3 5-6"/></svg>Enhanced treatment planning for cardiac conditions.</div>
      <div class="perk" style="left:182px;top:22px"><svg width="9" height="8" viewBox="0 0 10 8" fill="none" stroke="var(--teal)" stroke-width="2"><path d="M1 4l3 3 5-6"/></svg>Cutting-edge technology for precise imaging.</div>
      <div class="perk" style="left:20px;top:57px"><svg width="9" height="8" viewBox="0 0 10 8" fill="none" stroke="var(--teal)" stroke-width="2"><path d="M1 4l3 3 5-6"/></svg>Personalized care for better patient outcomes.</div>
      <div class="perk" style="left:182px;top:57px"><svg width="9" height="8" viewBox="0 0 10 8" fill="none" stroke="var(--teal)" stroke-width="2"><path d="M1 4l3 3 5-6"/></svg>Comprehensive fusion of PET and CT scans.</div>
      <div class="perk" style="left:20px;top:93px"><svg width="9" height="8" viewBox="0 0 10 8" fill="none" stroke="var(--teal)" stroke-width="2"><path d="M1 4l3 3 5-6"/></svg>Enhanced treatment planning for cardiac conditions.</div>
      <div class="perk" style="left:182px;top:93px"><svg width="9" height="8" viewBox="0 0 10 8" fill="none" stroke="var(--teal)" stroke-width="2"><path d="M1 4l3 3 5-6"/></svg>Minimized radiation exposure with optimized protocols.</div>
      <div class="perk" style="left:20px;top:125px"><svg width="9" height="8" viewBox="0 0 10 8" fill="none" stroke="var(--teal)" stroke-width="2"><path d="M1 4l3 3 5-6"/></svg>Enhanced detection and localization of cardiac issues.</div>
      <div class="perk" style="left:182px;top:125px"><svg width="9" height="8" viewBox="0 0 10 8" fill="none" stroke="var(--teal)" stroke-width="2"><path d="M1 4l3 3 5-6"/></svg>Experienced nuclear medicine specialists.</div>
    </div>
    <div class="tri" style="left:332px;top:394px"></div>
    <div class="tri" style="left:332px;top:406px"></div>
    <div class="tri" style="left:332px;top:418px"></div>
    <div class="tri" style="left:332px;top:430px"></div>
    <div class="mist" style="left:300px;top:448px;width:80px;height:60px;border-radius:10px"></div>
    <div class="frame" style="left:260px;top:478px;width:67px;height:30px"></div>
  </div>
</section>

</body>
</html>
```